paperwork
business cards and letterhead
Use same font as used in my logo
Dorian Pelfrey
CEO
247b Hollin Court Friendswood TX 77318 USA
dorian@mirelandbrookworks.com
www.pelvonaristo.com

```html
<!DOCTYPE html>
<html lang="en">
<head>
<meta charset="utf-8">
<title>Pelvon Aristo Stationery</title>
<link rel="stylesheet" href="https://fonts.googleapis.com/css2?family=Montserrat:wght@400;700&display=swap">
<style>
  :root{
    --bg:#e6e6e4;
    --paper:#ffffff;
    --ink:#4a4a4a;
    --ink-soft:#8a8a8a;
    --green:#5cb82e;
    --green-dark:#2f8a1c;
    --green-light:#a8dc5a;
    --grey-flap:#6e6e6e;
    --shadow:0 2px 6px rgba(0,0,0,.18);
  }
  *{box-sizing:border-box;margin:0;padding:0}
  html,body{width:1200px;height:466px;overflow:hidden}
  body{background:var(--bg);font-family:"Montserrat",sans-serif;color:var(--ink);position:relative}

  .sheet{position:absolute;background:var(--paper);box-shadow:var(--shadow);overflow:hidden}

  .brand{display:flex;flex-direction:column;align-items:center;gap:3px}
  .brand-row{display:flex;align-items:center;gap:5px}
  .brand-dot{width:14px;height:14px;border-radius:50%;background:var(--green)}
  .brand-name{font-weight:700;font-size:9px;letter-spacing:.5px;color:var(--ink)}
  .brand-tag{font-size:4px;letter-spacing:1px;color:var(--ink-soft)}

  .watermark{position:absolute;border-radius:50%;border:18px solid #f1f1f1;left:50%;transform:translateX(-50%)}

  .footer-band{position:absolute;left:0;right:0;bottom:0;height:14px;
    background:linear-gradient(180deg,var(--green-light),var(--green-dark))}
  .footer-text{position:absolute;left:0;right:0;font-size:4px;color:var(--ink-soft);text-align:center;letter-spacing:.3px}

  .contact{position:absolute;font-size:4px;line-height:6px;color:var(--ink-soft)}

  /* business cards */
  .card{left:12px;width:103px;height:62px}
  .card-front{top:96px}
  .card-back{top:235px}
  .card .footer-band{height:6px}
  .card-front .brand{position:absolute;top:18px;left:0;right:0}
  .card-front .brand-name{font-size:6px}
  .card-back .person{position:absolute;left:8px;top:10px;font-size:4.5px;line-height:6px}
  .card-back .person strong{display:block;font-size:5.5px;color:var(--ink)}
  .card-back .brand{position:absolute;left:8px;top:34px;align-items:flex-start}
  .card-back .brand-name{font-size:5px}
  .card-back .brand-dot{width:9px;height:9px}

  /* letterheads */
  .letterhead{top:29px;width:305px;height:379px}
  .letterhead-one{left:151px}
  .letterhead-two{left:492px}
  .letterhead .brand{position:absolute;top:18px;left:0;right:0}
  .letterhead .brand-dot{width:20px;height:20px}
  .letterhead .watermark{width:130px;height:130px;top:135px}
  .letterhead-one .contact{top:16px;right:20px}

  /* envelopes */
  .envelope-back{left:828px;top:29px;width:348px;height:212px;background:var(--paper)}
  .envelope-back .top-band{position:absolute;left:0;right:0;top:0;height:62px;
    background:linear-gradient(90deg,var(--green-dark),var(--green-light))}
  .envelope-back svg{position:absolute;left:0;top:0}
  .envelope-front{left:780px;top:283px;width:396px;height:144px}
  .envelope-front .brand{position:absolute;left:18px;top:14px;align-items:flex-start}
  .envelope-front .watermark{width:96px;height:96px;border-width:14px;top:22px;left:auto;right:30px;transform:none}
  .envelope-front .footer-band{height:10px}
</style>
</head>
<body>

<section class="sheet card card-front">
  <div class="brand">
    <div class="brand-row"><span class="brand-dot"></span><span class="brand-name">PELVON ARISTO</span></div>
    <span class="brand-tag">ENERGY SAVING LIGHTS</span>
  </div>
  <div class="footer-band"></div>
</section>

<section class="sheet card card-back">
  <div class="person"><strong>Dorian Pelfrey</strong>CEO<br>dorian@mirelandbrookworks.com<br>www.pelvonaristo.com</div>
  <div class="brand"><div class="brand-row"><span class="brand-dot"></span><span class="brand-name">PELVON ARISTO</span></div></div>
  <div class="footer-band"></div>
</section>

<section class="sheet letterhead letterhead-one">
  <div class="brand">
    <div class="brand-row"><span class="brand-dot"></span><span class="brand-name">PELVON ARISTO</span></div>
    <span class="brand-tag">ENERGY SAVING LIGHTS</span>
  </div>
  <div class="contact">247b Hollin Court<br>Friendswood TX 77318 USA<br>dorian@mirelandbrookworks.com<br>www.pelvonaristo.com</div>
  <div class="watermark"></div>
  <div class="footer-band"></div>
</section>

<section class="sheet letterhead letterhead-two">
  <div class="brand">
    <div class="brand-row"><span class="brand-dot"></span><span class="brand-name">PELVON ARISTO</span></div>
    <span class="brand-tag">ENERGY SAVING LIGHTS</span>
  </div>
  <div class="watermark"></div>
  <p class="footer-text" style="bottom:26px">247b Hollin Court Friendswood TX 77318 USA</p>
  <p class="footer-text" style="bottom:20px">dorian@mirelandbrookworks.com · www.pelvonaristo.com</p>
  <div class="footer-band"></div>
</section>

<section class="sheet envelope-back">
  <div class="top-band"></div>
  <svg width="348" height="212" viewBox="0 0 348 212" aria-hidden="true">
    <path d="M6 62 L174 128 L342 62 Z" fill="var(--grey-flap)"/>
    <path d="M0 212 L150 120 M348 212 L198 120" stroke="#dcdcdc" stroke-width="1" fill="none"/>
  </svg>
</section>

<section class="sheet envelope-front">
  <div class="brand">
    <div class="brand-row"><span class="brand-dot"></span><span class="brand-name">PELVON ARISTO</span></div>
    <span class="brand-tag">ENERGY SAVING LIGHTS</span>
  </div>
  <div class="watermark"></div>
  <div class="footer-band"></div>
</section>

</body>
</html>
```